Redesign of ademwolkhuis.nl – Clean, Trustworthy & User-Friendly Medical Equipment We...

PLEASE DO NOT CONTACT US OUTSIDE TEKENPLEIN.COM

We are looking for a talented and creative web designer to redesign the website www.ademwolkhuis.nl, a Dutch online store specializing in medical oxygen concentrators and related products.

The current website is functional but outdated in terms of design, structure, and user experience. We want a fresh, modern, and trustworthy design that reflects the medical and professional nature of the business, while also being clear, accessible, and easy to navigate for a broad audience — including elderly users and people with limited technical skills.

About the Business:
Ademwolkhuis.nl provides high-quality oxygen concentrators and accessories for both home and mobile use. The target audience includes individuals with respiratory conditions, healthcare professionals, and caregivers. Trust, clarity, and ease of use are key.

What We’re Looking For:
A clean and modern layout with a medical/professional feel
Strong focus on usability and accessibility
A design that works flawlessly on desktop and mobile (responsive)
Clear product presentation and easy-to-use navigation
Use of calming colors (e.g. white, light blue, grey tones) that reflect a medical/healthcare environment
Clear call-to-actions (e.g. “Vraag een offerte aan”, “Neem contact op”, etc.)
A design that builds trust and encourages inquiries or purchases

Pages We Need Designed:
Homepage
Product overview page (category)
Product detail page

Inspiration / Style Examples:
We’re looking for something in the style of:

Veltmar Careworks
Zorvan.nl
Welbrakkenshop.nl
Quint (for clean layout and spacing)

Deliverables:
Full desktop and mobile designs (Figma, Adobe PS)
All source files and assets used (fonts, icons, images, etc.)
Clean and organized layers
Design must be ready for implementation by our development team

Target Market(s)

Ademwolkhuis.nl targets both B2C and B2B audiences within the medical and healthcare sector in europe

Industry/Entity Type

Medical

Number of Pages Required

2 page

Font styles to use
Sans Serif

Requirements
Must have
• Clean and professional design, responsive layout (desktop and mobile), calming medical color scheme (e.g. light blue, white, grey), clear product presentation with specs and images, strong call-to-actions (e.g. "Vraag een offerte aan"), trust elements (certifications, reviews, support info), easy navigation for elderly and non-tech-savvy users, contact form easily accessible, SEO-friendly structure, fast loading design, privacy and regulatory compliance elements (e.g. CE mark info, medical disclaimers).
Should not have
• Overly complex design, dark or aggressive color schemes, small or hard-to-read fonts, cluttered layout, distracting animations, unnecessary pop-ups, autoplay videos or sounds, technical jargon without explanation, hidden contact options, slow-loading pages.

```html
<!DOCTYPE html>
<html lang="en">
<head>
<meta charset="utf-8">
<title>Ademwolkhuis – Oxygen Concentrators</title>
<link href="https://fonts.googleapis.com/css2?family=Inter:wght@400;500;600;700&family=Oswald:wght@500;600&display=swap" rel="stylesheet">
<style>
:root{
  --navy:#173a6a;
  --nav:#1b4a8e;
  --band:#1e4d86;
  --orange:#d2601a;
  --card:#f3f3f3;
  --soft:#f1f5fb;
  --text:#1b1b1b;
  --muted:#555;
  --footer-dark:#2b2b2b;
}
*{box-sizing:border-box;margin:0;padding:0}
html,body{width:1200px;height:4545px;overflow:hidden}
body{font-family:"Inter",sans-serif;color:var(--text);background:#fff;font-size:14px}
.display{font-family:"Oswald",sans-serif;font-weight:600;text-transform:uppercase;letter-spacing:.2px}
svg{display:block}

.topbar{height:35px;background:var(--navy);color:#fff;font-size:12px;display:flex;align-items:center;padding:0 100px;justify-content:space-between}
.topbar .grp{display:flex;gap:18px;align-items:center}
.topbar .it{display:flex;gap:5px;align-items:center}

.header{height:62px;display:flex;align-items:center;padding:0 100px;gap:30px}
.brand{font-weight:700;font-size:22px;color:var(--nav);display:flex;align-items:center;gap:8px;width:160px}
.brand .dot{width:14px;height:14px;border-radius:50%;background:var(--orange)}
.burger{width:24px}
.search{flex:1;max-width:500px;height:34px;border:1px solid #ddd;border-radius:17px;display:flex;align-items:center;justify-content:space-between;padding:0 4px 0 16px;font-size:11px;color:#888}
.search .go{width:28px;height:28px;border-radius:50%;background:var(--orange);display:flex;align-items:center;justify-content:center}
.hicons{margin-left:auto;display:flex;gap:22px;align-items:center;font-size:13px;font-weight:500}
.flag{width:22px;height:22px;border-radius:50%;background:#c8102e;border:3px solid #1f3f8a}

.mainnav{height:35px;background:var(--nav);display:flex;align-items:center;padding:0 100px;gap:40px;color:#fff;font-size:13px}

.hero{position:relative;height:627px;background:linear-gradient(100deg,#5b6f60 0%,#8c988d 35%,#c9cbc6 60%,#b4a9a6 100%);overflow:hidden}
.hero-photo{position:absolute;inset:0}
.hero h1{position:absolute;left:103px;top:185px;color:#fff;font-size:42px;line-height:52px;width:480px}
.hero .btn{position:absolute;left:100px;top:368px}
.dots{position:absolute;left:537px;top:576px;display:flex;gap:10px}
.dots span{width:12px;height:12px;border-radius:50%;border:1.5px solid #fff}
.dots span.on{background:#fff}

.btn{display:inline-block;background:var(--orange);color:#fff;font-size:14px;font-weight:500;padding:0 28px;height:34px;line-height:34px;border-radius:17px}

.cats{display:grid;grid-template-columns:repeat(3,383px);gap:13px 14px;padding:9px 11px 0 12px;height:850px}
.cat{background:var(--card);height:414px;text-align:center;padding-top:30px;position:relative}
.cat h3{font-size:21px;font-weight:600}
.cat p{font-size:14px;margin:8px 0 14px}
.cat .btn{height:36px;line-height:36px;padding:0 32px}
.cat .ph{position:absolute;left:95px;right:95px;top:160px;bottom:16px;border-radius:8px}

.sec-title{text-align:center;font-size:28px;line-height:40px;height:40px}
.products{display:grid;grid-template-columns:repeat(4,240px);gap:24px 12px;padding:0 100px}
.pcard{height:334px;border:1px solid #eee;border-radius:4px;position:relative}
.pcard .img{position:absolute;left:12px;right:12px;top:0;height:210px;background:var(--card);display:flex;align-items:center;justify-content:center}
.pcard .img .ph{width:100px;height:165px;border-radius:12px}
.pcard h4{position:absolute;left:6px;right:6px;top:220px;font-size:15px;font-weight:600;line-height:19px}
.pcard .desc{position:absolute;left:6px;right:6px;top:260px;font-size:9.5px;line-height:13px;color:var(--muted)}
.pcard .price{position:absolute;left:6px;top:300px;font-size:21px;line-height:26px;font-weight:600}
.pcard .cart{position:absolute;right:14px;top:297px;width:32px;height:32px;border-radius:50%;background:var(--orange);display:flex;align-items:center;justify-content:center}
.ph-white{background:linear-gradient(#fafafa,#dcdcdc)}
.ph-dark{background:linear-gradient(#4b524e,#2c312e)}
.ph-port{background:linear-gradient(#f4f4f4,#d6dbe3)}
.ph-blue{background:linear-gradient(#6aa3da,#3f7fbf)}

.arrows{display:flex;gap:12px;justify-content:center;height:42px}
.arrows span{width:42px;height:42px;border-radius:50%;border:1.5px solid #ccc;display:flex;align-items:center;justify-content:center}
.arrows span.on{border-color:#222}

.brands{background:var(--soft);height:296px;padding-top:52px}
.brandrow{display:grid;grid-template-columns:repeat(5,191px);gap:10px;padding:0 100px;margin:22px 0 20px}
.brandrow div{height:95px;background:#fff;display:flex;align-items:center;justify-content:center;font-weight:600;font-size:20px;color:var(--nav)}

.testi{background:var(--soft);height:473px;padding-top:58px;margin-top:77px}
.tgrid{display:grid;grid-template-columns:repeat(3,322px);gap:15px;padding:0 100px;margin:12px 0 17px}
.tcard{background:#fff;height:242px;padding:20px 18px;position:relative}
.stars{display:flex;gap:3px}
.tcard p{font-style:italic;font-size:12.5px;line-height:22px;color:#444;margin-top:12px}
.who{position:absolute;left:18px;right:18px;bottom:16px;display:flex;align-items:center;gap:10px}
.avatar{width:40px;height:40px;border-radius:50%;background:#b9a898}
.who b{font-size:14px;font-weight:600;display:block}
.who small{font-size:11px}
.who .src{margin-left:auto;width:20px;height:20px;border-radius:50%;border:3px solid #4285c4}

.news{background:var(--navy);height:291px;text-align:center;color:#fff;padding-top:66px}
.news h2{font-size:40px;line-height:52px}
.news p{font-size:16px;line-height:21px;margin-top:6px}
.nform{width:684px;height:44px;margin:26px auto 0;background:#fff;border-radius:22px;display:flex;align-items:center;justify-content:space-between;padding-left:40px;font-size:14px;color:#555}
.nform .btn{height:44px;line-height:44px;border-radius:22px;width:190px;padding:0;text-align:center}

.perks{background:var(--band);height:115px;display:flex;align-items:center;justify-content:space-between;padding:0 100px;color:#fff;font-size:17px;font-weight:600}
.perks div{display:flex;align-items:center;gap:14px}

.footer{height:260px;display:flex;padding:26px 0 0 100px;overflow:hidden}
.fcol h5{font-family:"Oswald",sans-serif;font-size:20px;line-height:26px;font-weight:600;margin-bottom:8px}
.fcol a{display:block;font-size:16px;color:#222;text-decoration:none;line-height:34px}
.pay{display:flex;gap:8px;margin-top:6px}
.pay span{width:40px;height:26px;border:1px solid #ddd;border-radius:3px;font-size:8px;display:flex;align-items:center;justify-content:center;color:#333}
.social{display:flex;gap:10px}
.social span{width:33px;height:33px;border-radius:50%;background:var(--navy)}
.copy{height:58px;background:var(--footer-dark);color:#fff;text-align:center;line-height:58px;font-size:16px}
</style>
</head>
<body>

<div class="topbar">
  <div class="grp">
    <span class="it"><svg width="13" height="13" viewBox="0 0 24 24"><path fill="#fff" d="M6.6 10.8a15 15 0 006.6 6.6l2.2-2.2c.3-.3.7-.4 1-.2 1.1.4 2.3.6 3.6.6.6 0 1 .4 1 1V20c0 .6-.4 1-1 1A17 17 0 013 4c0-.6.4-1 1-1h3.5c.6 0 1 .4 1 1 0 1.3.2 2.5.6 3.6.1.3 0 .7-.2 1z"/></svg>+31-701234567</span>
    <span class="it"><svg width="14" height="12" viewBox="0 0 24 20"><rect x="1" y="1" width="22" height="18" rx="2" fill="none" stroke="#fff" stroke-width="2"/><path d="M2 3l10 8 10-8" fill="none" stroke="#fff" stroke-width="2"/></svg>info@ademwolkhuis.nl</span>
  </div>
  <span class="it"><svg width="16" height="11" viewBox="0 0 24 16"><path d="M1 2h13v10H1zM14 6h5l4 4v2h-9" fill="none" stroke="#fff" stroke-width="1.6"/><circle cx="6" cy="13" r="2" fill="#fff"/><circle cx="18" cy="13" r="2" fill="#fff"/></svg>Free shipping from €250</span>
  <div class="grp">
    <span class="it"><svg width="11" height="14" viewBox="0 0 16 22"><path d="M8 1a7 7 0 017 7c0 5-7 13-7 13S1 13 1 8a7 7 0 017-7z" fill="none" stroke="#fff" stroke-width="2"/><circle cx="8" cy="8" r="2.5" fill="#fff"/></svg>Store Locator</span>
    <span class="it"><svg width="12" height="12" viewBox="0 0 20 20"><path d="M3 6h14l-1 12H4z" fill="none" stroke="#fff" stroke-width="2"/><path d="M7 6V4a3 3 0 016 0v2" fill="none" stroke="#fff" stroke-width="2"/></svg>Shop</span>
    <span class="it"><svg width="12" height="12" viewBox="0 0 20 20"><circle cx="10" cy="6" r="4" fill="none" stroke="#fff" stroke-width="2"/><path d="M2 19c0-4 4-6 8-6s8 2 8 6" fill="none" stroke="#fff" stroke-width="2"/></svg>My Account</span>
  </div>
</div>

<header class="header">
  <div class="brand"><span class="dot"></span>Ademwolkhuis</div>
  <svg class="burger" width="24" height="18" viewBox="0 0 24 18"><path d="M0 1h24M0 9h24M0 17h24" stroke="#222" stroke-width="2"/></svg>
  <div class="search"><span>Search products...</span><span class="go"><svg width="14" height="14" viewBox="0 0 20 20"><circle cx="8" cy="8" r="6" fill="none" stroke="#fff" stroke-width="2"/><path d="M13 13l5 5" stroke="#fff" stroke-width="2"/></svg></span></div>
  <div class="hicons">
    <span class="flag"></span>
    <svg width="22" height="18" viewBox="0 0 24 20"><path d="M2 6h18l-4-4M22 14H4l4 4" fill="none" stroke="#222" stroke-width="2"/></svg>
    <svg width="24" height="22" viewBox="0 0 24 22"><path d="M12 20S2 14 2 7a5 5 0 0110-1 5 5 0 0110 1c0 7-10 13-10 13z" fill="none" stroke="#222" stroke-width="2"/></svg>
    <span style="display:flex;gap:6px;align-items:center"><svg width="20" height="22" viewBox="0 0 20 22"><path d="M2 6h16l-1 15H3z" fill="none" stroke="#222" stroke-width="2"/><path d="M6 6V4a4 4 0 018 0v2" fill="none" stroke="#222" stroke-width="2"/></svg>€0.00</span>
  </div>
</header>

<nav class="mainnav">
  <span>Oxygen Concentrator ▾</span><span>Portable Oxygen Concentrator ▾</span><span>Supplies ▾</span><span>Filters</span><span>Rental</span><span>Manufactures</span><span>Flowsplitter</span><span>More ▾</span>
</nav>

<section class="hero">
  <div class="hero-photo" role="img" aria-label="Woman resting on a cushion with a nasal cannula, reading beside a home oxygen concentrator"></div>
  <h1 class="display">Reliable oxygen concentrators for home and travel</h1>
  <span class="btn">Shop Now</span>
  <div class="dots"><span></span><span></span><span></span><span class="on"></span><span></span><span></span></div>
</section>

<section class="cats">
  <div class="cat"><h3>Oxygen Concentrator</h3><p>Finibus Bonorum Et Malorum</p><span class="btn">Shop Now</span><div class="ph ph-white" role="img" aria-label="Stationary oxygen concentrator"></div></div>
  <div class="cat"><h3>Portable Oxygen Concentrator</h3><p>Finibus Bonorum Et Malorum</p><span class="btn">Shop Now</span><div class="ph ph-dark" role="img" aria-label="Portable oxygen concentrator on wheels"></div></div>
  <div class="cat"><h3>Supplies</h3><p>Finibus Bonorum Et Malorum</p><span class="btn">Shop Now</span><div class="ph" style="background:linear-gradient(#eef1f4,#dfe4ea)" role="img" aria-label="Clear nasal cannula tubing"></div></div>
  <div class="cat"><h3>FlowSplitter</h3><p>Finibus Bonorum Et Malorum</p><span class="btn">Shop Now</span><div class="ph" style="background:linear-gradient(#39495e,#1f2a38)" role="img" aria-label="Concentrator with flow splitter unit"></div></div>
  <div class="cat"><h3>Filters</h3><p>Finibus Bonorum Et Malorum</p><span class="btn">Shop Now</span><div class="ph" style="background:linear-gradient(#333,#111)" role="img" aria-label="Stack of black foam filters"></div></div>
  <div class="cat"><h3>Oxygen Filling Station</h3><p>Finibus Bonorum Et Malorum</p><span class="btn">Shop Now</span><div class="ph" style="background:linear-gradient(#2a2a2a,#0f0f0f)" role="img" aria-label="Oxygen filling station"></div></div>
</section>

<h2 class="sec-title display" style="margin-top:51px">Recommended Products</h2>
<section class="products" style="margin-top:23px">
  <div class="pcard"><div class="img"><div class="ph ph-white" role="img" aria-label="White oxygen concentrator"></div></div><h4>Aerfill oxygen filling station pulse</h4><p class="desc">This easy-to-use oxygen filling station extracts and pressurizes room</p><span class="price">€3,270.00</span><span class="cart"><svg width="14" height="16" viewBox="0 0 20 22"><path d="M2 6h16l-1 15H3z" fill="none" stroke="#fff" stroke-width="2"/><path d="M6 6V4a4 4 0 018 0v2" fill="none" stroke="#fff" stroke-width="2"/></svg></span></div>
  <div class="pcard"><div class="img"><div class="ph ph-dark" role="img" aria-label="Dark grey oxygen concentrator"></div></div><h4>Aerfill oxygen filling station pulse</h4><p class="desc">This easy-to-use oxygen filling station extracts and pressurizes room</p><span class="price">€3,270.00</span><span class="cart"><svg width="14" height="16" viewBox="0 0 20 22"><path d="M2 6h16l-1 15H3z" fill="none" stroke="#fff" stroke-width="2"/><path d="M6 6V4a4 4 0 018 0v2" fill="none" stroke="#fff" stroke-width="2"/></svg></span></div>
  <div class="pcard"><div class="img"><div class="ph ph-port" role="img" aria-label="Compact portable concentrator"></div></div><h4>Aerfill oxygen filling station pulse</h4><p class="desc">This easy-to-use oxygen filling station extracts and pressurizes room</p><span class="price">€3,270.00</span><span class="cart"><svg width="14" height="16" viewBox="0 0 20 22"><path d="M2 6h16l-1 15H3z" fill="none" stroke="#fff" stroke-width="2"/><path d="M6 6V4a4 4 0 018 0v2" fill="none" stroke="#fff" stroke-width="2"/></svg></span></div>
  <div class="pcard"><div class="img"><div class="ph ph-blue" role="img" aria-label="Light blue oxygen concentrator"></div></div><h4>Aerfill oxygen filling station pulse</h4><p class="desc">This easy-to-use oxygen filling station extracts and pressurizes room</p><span class="price">€3,270.00</span><span class="cart"><svg width="14" height="16" viewBox="0 0 20 22"><path d="M2 6h16l-1 15H3z" fill="none" stroke="#fff" stroke-width="2"/><path d="M6 6V4a4 4 0 018 0v2" fill="none" stroke="#fff" stroke-width="2"/></svg></span></div>
</section>
<div class="arrows" style="margin:29px 0 38px"><span><svg width="18" height="10" viewBox="0 0 18 10"><path d="M17 5H1m4-4L1 5l4 4" fill="none" stroke="#bbb" stroke-width="1.5"/></svg></span><span class="on"><svg width="18" height="10" viewBox="0 0 18 10"><path d="M1 5h16m-4-4l4 4-4 4" fill="none" stroke="#222" stroke-width="1.5"/></svg></span></div>

<section class="brands">
  <h2 class="sec-title display">Brand We Carry</h2>
  <div class="brandrow"><div>Luvena</div><div>Medora</div><div>Halvik</div><div>Brevo Air</div><div style="font-size:15px">Veltmar Careworks</div></div>
  <div class="arrows"><span><svg width="18" height="10" viewBox="0 0 18 10"><path d="M17 5H1m4-4L1 5l4 4" fill="none" stroke="#bbb" stroke-width="1.5"/></svg></span><span class="on"><svg width="18" height="10" viewBox="0 0 18 10"><path d="M1 5h16m-4-4l4 4-4 4" fill="none" stroke="#222" stroke-width="1.5"/></svg></span></div>
</section>

<h2 class="sec-title display" style="margin-top:54px">Featured Proudct</h2>
<section class="products" style="margin-top:23px">
  <div class="pcard"><div class="img"><div class="ph ph-white" role="img" aria-label="White oxygen concentrator"></div></div><h4>Aerfill oxygen filling station pulse</h4><p class="desc">This easy-to-use oxygen filling station extracts and pressurizes room</p><span class="price">€3,270.00</span><span class="cart"><svg width="14" height="16" viewBox="0 0 20 22"><path d="M2 6h16l-1 15H3z" fill="none" stroke="#fff" stroke-width="2"/><path d="M6 6V4a4 4 0 018 0v2" fill="none" stroke="#fff" stroke-width="2"/></svg></span></div>
  <div class="pcard"><div class="img"><div class="ph ph-dark" role="img" aria-label="Dark grey oxygen concentrator"></div></div><h4>Aerfill oxygen filling station pulse</h4><p class="desc">This easy-to-use oxygen filling station extracts and pressurizes room</p><span class="price">€3,270.00</span><span class="cart"><svg width="14" height="16" viewBox="0 0 20 22"><path d="M2 6h16l-1 15H3z" fill="none" stroke="#fff" stroke-width="2"/><path d="M6 6V4a4 4 0 018 0v2" fill="none" stroke="#fff" stroke-width="2"/></svg></span></div>
  <div class="pcard"><div class="img"><div class="ph ph-port" role="img" aria-label="Compact portable concentrator"></div></div><h4>Aerfill oxygen filling station pulse</h4><p class="desc">This easy-to-use oxygen filling station extracts and pressurizes room</p><span class="price">€3,270.00</span><span class="cart"><svg width="14" height="16" viewBox="0 0 20 22"><path d="M2 6h16l-1 15H3z" fill="none" stroke="#fff" stroke-width="2"/><path d="M6 6V4a4 4 0 018 0v2" fill="none" stroke="#fff" stroke-width="2"/></svg></span></div>
  <div class="pcard"><div class="img"><div class="ph ph-blue" role="img" aria-label="Light blue oxygen concentrator"></div></div><h4>Aerfill oxygen filling station pulse</h4><p class="desc">This easy-to-use oxygen filling station extracts and pressurizes room</p><span class="price">€3,270.00</span><span class="cart"><svg width="14" height="16" viewBox="0 0 20 22"><path d="M2 6h16l-1 15H3z" fill="none" stroke="#fff" stroke-width="2"/><path d="M6 6V4a4 4 0 018 0v2" fill="none" stroke="#fff" stroke-width="2"/></svg></span></div>
  <div class="pcard"><div class="img"><div class="ph ph-white" role="img" aria-label="White oxygen concentrator"></div></div><h4>Aerfill oxygen filling station pulse</h4><p class="desc">This easy-to-use oxygen filling station extracts and pressurizes room</p><span class="price">€3,270.00</span><span class="cart"><svg width="14" height="16" viewBox="0 0 20 22"><path d="M2 6h16l-1 15H3z" fill="none" stroke="#fff" stroke-width="2"/><path d="M6 6V4a4 4 0 018 0v2" fill="none" stroke="#fff" stroke-width="2"/></svg></span></div>
  <div class="pcard"><div class="img"><div class="ph ph-dark" role="img" aria-label="Dark grey oxygen concentrator"></div></div><h4>Aerfill oxygen filling station pulse</h4><p class="desc">This easy-to-use oxygen filling station extracts and pressurizes room</p><span class="price">€3,270.00</span><span class="cart"><svg width="14" height="16" viewBox="0 0 20 22"><path d="M2 6h16l-1 15H3z" fill="none" stroke="#fff" stroke-width="2"/><path d="M6 6V4a4 4 0 018 0v2" fill="none" stroke="#fff" stroke-width="2"/></svg></span></div>
  <div class="pcard"><div class="img"><div class="ph ph-port" role="img" aria-label="Compact portable concentrator"></div></div><h4>Aerfill oxygen filling station pulse</h4><p class="desc">This easy-to-use oxygen filling station extracts and pressurizes room</p><span class="price">€3,270.00</span><span class="cart"><svg width="14" height="16" viewBox="0 0 20 22"><path d="M2 6h16l-1 15H3z" fill="none" stroke="#fff" stroke-width="2"/><path d="M6 6V4a4 4 0 018 0v2" fill="none" stroke="#fff" stroke-width="2"/></svg></span></div>
  <div class="pcard"><div class="img"><div class="ph ph-blue" role="img" aria-label="Light blue oxygen concentrator"></div></div><h4>Aerfill oxygen filling station pulse</h4><p class="desc">This easy-to-use oxygen filling station extracts and pressurizes room</p><span class="price">€3,270.00</span><span class="cart"><svg width="14" height="16" viewBox="0 0 20 22"><path d="M2 6h16l-1 15H3z" fill="none" stroke="#fff" stroke-width="2"/><path d="M6 6V4a4 4 0 018 0v2" fill="none" stroke="#fff" stroke-width="2"/></svg></span></div>
</section>

<section class="testi">
  <h2 class="sec-title display">Customer Testimonials</h2>
  <div class="tgrid">
    <div class="tcard"><div class="stars"><svg width="100" height="18" viewBox="0 0 100 18"><g fill="#173a6a"><path id="st" d="M9 1l2.4 5.4 5.6.5-4.3 3.8 1.3 5.7L9 13.4 4 16.4l1.3-5.7L1 6.9l5.6-.5z"/><use href="#st" x="20"/><use href="#st" x="40"/><use href="#st" x="60"/><use href="#st" x="80"/></g></svg></div><p>Sed ut perspiciatis unde omnis iste us error sit voluptatem accusaloremque laudantium, totam rem aperiam, eaque ipsa quae ab illo inventore veritatis et quasi arctecto beatae vitae dicta sunt explicabo.</p><div class="who"><span class="avatar" role="img" aria-label="Reviewer portrait"></span><span><b>Mara Jensen</b><small>Project Manger</small></span><span class="src"></span></div></div>
    <div class="tcard"><div class="stars"><svg width="100" height="18" viewBox="0 0 100 18"><g fill="#173a6a"><use href="#st"/><use href="#st" x="20"/><use href="#st" x="40"/><use href="#st" x="60"/><use href="#st" x="80"/></g></svg></div><p>Sed ut perspiciatis unde omnis iste us error sit voluptatem accusaloremque laudantium, totam rem aperiam, eaque ipsa quae ab illo inventore veritatis et quasi arctecto beatae vitae dicta sunt explicabo.</p><div class="who"><span class="avatar" role="img" aria-label="Reviewer portrait"></span><span><b>Mara Jensen</b><small>Project Manger</small></span><span class="src"></span></div></div>
    <div class="tcard"><div class="stars"><svg width="100" height="18" viewBox="0 0 100 18"><g fill="#173a6a"><use href="#st"/><use href="#st" x="20"/><use href="#st" x="40"/><use href="#st" x="60"/><use href="#st" x="80"/></g></svg></div><p>Sed ut perspiciatis unde omnis iste us error sit voluptatem accusaloremque laudantium, totam rem aperiam, eaque ipsa quae ab illo inventore veritatis et quasi arctecto beatae vitae dicta sunt explicabo.</p><div class="who"><span class="avatar" role="img" aria-label="Reviewer portrait"></span><span><b>Mara Jensen</b><small>Project Manger</small></span><span class="src"></span></div></div>
  </div>
  <div class="arrows"><span><svg width="18" height="10" viewBox="0 0 18 10"><path d="M17 5H1m4-4L1 5l4 4" fill="none" stroke="#bbb" stroke-width="1.5"/></svg></span><span class="on"><svg width="18" height="10" viewBox="0 0 18 10"><path d="M1 5h16m-4-4l4 4-4 4" fill="none" stroke="#222" stroke-width="1.5"/></svg></span></div>
</section>

<section class="news">
  <h2 class="display">Join &amp; Get 10% Off Your First Order</h2>
  <p>Sign up for the Ademwolkhuis BV newsletter to hear about new oxygen concentrators<br>seals, special sales &amp; more.</p>
  <div class="nform"><span>Email Address</span><span class="btn">Subscribe</span></div>
</section>

<section class="perks">
  <div><svg width="50" height="30" viewBox="0 0 50 30"><path d="M2 4h28v18H2zM30 10h10l7 7v5H30" fill="none" stroke="#fff" stroke-width="2"/><circle cx="12" cy="24" r="4" fill="#1e4d86" stroke="#fff" stroke-width="2"/><circle cx="38" cy="24" r="4" fill="#1e4d86" stroke="#fff" stroke-width="2"/></svg>Free Shipping</div>
  <div><svg width="46" height="40" viewBox="0 0 46 40"><path d="M4 10l16-8 16 8v18l-16 8-16-8z" fill="none" stroke="#fff" stroke-width="2"/><path d="M4 10l16 8 16-8M20 18v18" fill="none" stroke="#fff" stroke-width="2"/><circle cx="36" cy="30" r="7" fill="#1e4d86" stroke="#fff" stroke-width="2"/><path d="M33 30l2 2 4-4" fill="none" stroke="#fff" stroke-width="2"/></svg>Oxygen Concentrator</div>
  <div><svg width="50" height="30" viewBox="0 0 50 30"><path d="M2 4h28v18H2zM30 10h10l7 7v5H30" fill="none" stroke="#fff" stroke-width="2"/><circle cx="12" cy="24" r="4" fill="#1e4d86" stroke="#fff" stroke-width="2"/><circle cx="38" cy="24" r="4" fill="#1e4d86" stroke="#fff" stroke-width="2"/></svg>Safe Shopping</div>
  <div><svg width="42" height="42" viewBox="0 0 42 42"><circle cx="21" cy="21" r="18" fill="none" stroke="#fff" stroke-width="2" stroke-dasharray="4 3"/><circle cx="21" cy="16" r="5" fill="none" stroke="#fff" stroke-width="2"/><path d="M11 32c0-6 5-9 10-9s10 3 10 9" fill="none" stroke="#fff" stroke-width="2"/></svg>22 Years Of Experience</div>
</section>

<footer class="footer">
  <div class="fcol" style="width:188px"><h5>ABOUT US</h5><a>About Us</a><a>Dispatch</a><a>Commercial</a></div>
  <div class="fcol" style="width:275px"><h5>CUSTOMER SERVICE</h5><a>Contact</a><a>Warranty And Service</a><a>Returns</a><a>Site Map</a><a>To Notice</a></div>
  <div class="fcol" style="width:325px"><h5>SHIPPING &amp; RETURNS</h5><a>Shipping Policy</a><a>Return Policy</a><h5 style="margin-top:10px">SHIPPING &amp; RETURNS</h5><a>Privacy Policy</a><a>General Terms &amp; Conditions</a></div>
  <div class="fcol"><h5>PAYMENT ACCEPT</h5><div class="pay"><span>Card</span><span>Debit</span><span>Wallet</span><span>Bank</span></div><h5 style="margin-top:40px">FOLLOW US</h5><div class="social"><span></span><span></span><span></span><span></span></div></div>
</footer>
<div class="copy">Copyright © 2003-2025, Ademwolkhuis BV, All Rights Reserved</div>

</body>
</html>
```